Local Flower Farm Needs Business Card Design

I need business cards designed for a flower farm based in Eudora, Kansas.
Business Info:
We are a local cut flower farm located in Eudora, Kansas, founded by Darla Hoffstrom. What started as a passion for agriculture and search for more joy in daily life has blossomed into a small business dedicated to providing the community with beautiful, fresh, and sustainable flowers. We specialize in local, seasonal blooms, ensuring that every petal reflects the care and dedication we pour into our craft. Our mission is to deliver the highest quality flowers directly to our customers through local farmers markets and to florists who share our commitment to sustainability. Join us in celebrating the beauty of nature, one bloom at a time!
Contact Details:
Darla Hoffstrom
Owner
Phone 913-555-0147
Facebook: Lorabelle Quinn Blossoms
Instagram: @LorabelleQuinnBlossoms
Website: LorabelleQuinnBlossoms.example
Target Market(s)
Wholesale to Florists and Direct to Consumer via Farmers Market
Industry/Entity Type
Florist, Farm
Contact Information for Business Card
Name, Contact Info, Logo
Look and feel

```html
<!DOCTYPE html>
<html lang="en">
<head>
<meta charset="utf-8">
<title>Lorabelle Quinn Blossoms – Business Card</title>
<link rel="stylesheet" href="https://fonts.googleapis.com/css2?family=EB+Garamond:wght@400&family=Lato:wght@400&display=swap">
<style>
  :root {
    --stage: #3a3a3b;
    --teal-center: #0f4a52;
    --teal-edge: #092b30;
    --card-white: #ffffff;
    --ink: #1b3135;
    --ink-soft: #2a2a2a;
    --line-light: rgba(255,255,255,0.85);
    --serif: "EB Garamond", Georgia, serif;
    --sans: "Lato", Arial, sans-serif;
  }
  * { box-sizing: border-box; margin: 0; padding: 0; }
  html, body { width: 1200px; height: 1000px; overflow: hidden; }
  body { background: var(--stage); position: relative; }

  .card {
    position: absolute;
    left: 200px;
    width: 801px;
    height: 457px;
    border-radius: 20px;
    overflow: hidden;
  }
  .card--front {
    top: 22px;
    background: radial-gradient(ellipse at 50% 35%, var(--teal-center) 0%, var(--teal-edge) 100%);
  }
  .card--back {
    top: 502px;
    background: var(--card-white);
  }

  .brand-seal {
    position: absolute;
    border-radius: 50%;
    display: flex;
    align-items: center;
    justify-content: center;
    text-align: center;
    font-family: var(--serif);
    font-weight: 400;
    text-transform: uppercase;
  }
  .brand-seal--front {
    left: 257px; top: 85px;
    width: 287px; height: 287px;
    border: 1.5px solid var(--line-light);
    color: #ffffff;
    font-size: 30px;
    letter-spacing: 3px;
    line-height: 1.25;
  }
  .brand-seal--back {
    left: 615px; top: 28px;
    width: 156px; height: 156px;
    border: 1px solid var(--ink);
    color: var(--ink);
    font-size: 16px;
    letter-spacing: 1.5px;
    line-height: 1.25;
  }

  .identity {
    position: absolute;
    left: 27px; top: 302px;
    display: flex;
    align-items: center;
    height: 44px;
  }
  .identity__name {
    font-family: var(--serif);
    font-size: 29px;
    color: var(--ink);
    letter-spacing: 0.3px;
    padding-right: 13px;
    border-right: 1.5px solid var(--ink);
    line-height: 44px;
  }
  .identity__role {
    font-family: var(--serif);
    font-size: 23px;
    color: var(--ink);
    padding-left: 12px;
  }

  .contacts {
    position: absolute;
    left: 28px; top: 366px;
    display: grid;
    grid-template-columns: 357px 360px;
    row-gap: 3px;
  }
  .contact {
    display: flex;
    align-items: center;
    gap: 6px;
    font-family: var(--sans);
    font-size: 22px;
    color: var(--ink-soft);
    height: 26px;
  }
  .contact__icon { width: 26px; height: 26px; flex: none; }
</style>
</head>
<body>
  <section class="card card--front">
    <div class="brand-seal brand-seal--front">Lorabelle<br>Quinn<br>Blossoms</div>
  </section>

  <section class="card card--back">
    <div class="brand-seal brand-seal--back">Lorabelle<br>Quinn<br>Blossoms</div>

    <div class="identity">
      <span class="identity__name">DARLA HOFFSTROM</span>
      <span class="identity__role">Owner</span>
    </div>

    <div class="contacts">
      <div class="contact">
        <svg class="contact__icon" viewBox="0 0 26 26" aria-hidden="true">
          <rect x="1.5" y="1.5" width="23" height="23" rx="3" fill="none" stroke="#1b3135" stroke-width="2"/>
          <path d="M8 6.5 l2.5 0 1.2 3.5 -1.7 1.3 c0.9 2 2.3 3.4 4.2 4.3 l1.3 -1.7 3.5 1.2 0 2.5 c0 0.8 -0.7 1.4 -1.5 1.4 C11 18.8 6.6 14.4 6.6 8 c0 -0.8 0.6 -1.5 1.4 -1.5z" fill="#1b3135"/>
        </svg>
        <span>913-555-0147</span>
      </div>
      <div class="contact">
        <svg class="contact__icon" viewBox="0 0 26 26" aria-hidden="true">
          <rect x="1.5" y="1.5" width="23" height="23" rx="3" fill="none" stroke="#1b3135" stroke-width="2"/>
        </svg>
        <span>Lorabelle Quinn Blossoms</span>
      </div>
      <div class="contact">
        <svg class="contact__icon" viewBox="0 0 26 26" aria-hidden="true">
          <rect x="1.5" y="1.5" width="23" height="23" rx="3" fill="none" stroke="#1b3135" stroke-width="2"/>
        </svg>
        <span>@LorabelleQuinnBlossoms</span>
      </div>
      <div class="contact">
        <svg class="contact__icon" viewBox="0 0 26 26" aria-hidden="true">
          <rect x="1.5" y="1.5" width="23" height="23" rx="3" fill="none" stroke="#1b3135" stroke-width="2"/>
          <circle cx="13" cy="13" r="6.5" fill="none" stroke="#1b3135" stroke-width="1.6"/>
          <ellipse cx="13" cy="13" rx="2.8" ry="6.5" fill="none" stroke="#1b3135" stroke-width="1.3"/>
          <line x1="6.5" y1="13" x2="19.5" y2="13" stroke="#1b3135" stroke-width="1.3"/>
        </svg>
        <span>LorabelleQuinnBlossoms.example</span>
      </div>
    </div>
  </section>
</body>
</html>
```